Business card for Sports Apparel business

DOUBLE SIDED DESIGN
We need business cards for a new sports apparel business. We are developing a protective headband for soccer initially.
Corvell is focused on designing and developing head protection products to reduce the likelihood of concussion when playing sports. Exploring and understanding medical insights, material science research, current and former players experiences and governing bodies guidelines has allowed Corvell to develop the safety, style, form and function requirements of a suitable product to bring to market.
Target Market(s)
Mums buying kits for the sons and daughters. Amateur footballers.
Industry/Entity Type
Sporting Good
Contact Information for Business Card
Martin Ashgrove - CEO
Mobile: +44 7391608254
Email: martin@corvell.co.uk
Tel: 0208 5143927
Helena Pardoe - COO
Mob: +44 7356 409183
Email: helena@corvell.co.uk
Tel: 0208 5143927
Duncan Wyvern - CCO
Mob: +44 7468 230517
Email: duncan@corvell.co.uk
Tel: 0208 5143927
Look and feel

```html
<!DOCTYPE html>
<html lang="en">
<head>
<meta charset="utf-8">
<title>Corvell business card</title>
<link href="https://fonts.googleapis.com/css2?family=Montserrat:wght@400;500;700&display=swap" rel="stylesheet">
<style>
  :root {
    --page-bg: #1e1e1e;
    --brand-blue: #0b5a92;
    --card-white: #ffffff;
    --text-grey: #5e6468;
    --rule-blue: #1d5f96;
  }
  html, body {
    margin: 0;
    width: 1200px;
    height: 852px;
    overflow: hidden;
    background: var(--page-bg);
    font-family: "Montserrat", sans-serif;
  }
  .sheet {
    position: relative;
    width: 1200px;
    height: 852px;
    display: flex;
    flex-direction: column;
    align-items: center;
    justify-content: center;
    gap: 40px;
  }
  .card {
    position: relative;
    width: 640px;
    height: 366px;
    box-sizing: border-box;
    box-shadow: 0 8px 24px rgba(0,0,0,0.45);
  }
  .card-front {
    background: var(--brand-blue);
    display: flex;
    align-items: center;
    justify-content: center;
  }
  .wordmark {
    display: flex;
    align-items: center;
    gap: 14px;
    font-weight: 700;
    letter-spacing: 0.04em;
    text-transform: uppercase;
  }
  .wordmark-square {
    display: block;
    background: currentColor;
  }
  .card-front .wordmark {
    color: var(--card-white);
    font-size: 58px;
  }
  .card-front .wordmark-square { width: 34px; height: 34px; }
  .card-back {
    background: var(--card-white);
    padding: 0 44px;
  }
  .card-back .wordmark {
    position: absolute;
    left: 44px;
    top: 62px;
    color: var(--text-grey);
    font-size: 34px;
  }
  .card-back .wordmark-square {
    width: 20px; height: 20px;
    background: var(--brand-blue);
  }
  .person {
    position: absolute;
    left: 150px;
    top: 218px;
  }
  .person-name {
    margin: 0;
    color: var(--brand-blue);
    font-weight: 700;
    font-size: 17px;
    letter-spacing: 0.03em;
    text-transform: uppercase;
  }
  .person-role {
    margin: 2px 0 0 18px;
    color: var(--text-grey);
    font-size: 13px;
    font-weight: 400;
  }
  .rule {
    position: absolute;
    left: 150px;
    right: 28px;
    top: 270px;
    height: 1.5px;
    background: var(--rule-blue);
  }
  .contact-line {
    position: absolute;
    left: 150px;
    top: 284px;
    margin: 0;
    font-size: 11.5px;
    color: var(--text-grey);
    white-space: nowrap;
  }
  .contact-label {
    color: var(--brand-blue);
    font-weight: 700;
  }
  .contact-sep { margin: 0 5px; }
</style>
</head>
<body>
<main class="sheet">
  <section class="card card-front" aria-label="Card front">
    <div class="wordmark"><span class="wordmark-square"></span>Corvell</div>
  </section>

  <section class="card card-back" aria-label="Card back">
    <div class="wordmark"><span class="wordmark-square"></span>Corvell</div>
    <div class="person">
      <p class="person-name">Martin Ashgrove</p>
      <p class="person-role">CEO</p>
    </div>
    <div class="rule"></div>
    <p class="contact-line">
      <span class="contact-label">P:</span> 0208 5143927<span class="contact-sep">|</span><span class="contact-label">M:</span> +44 7391608254<span class="contact-sep">|</span><span class="contact-label">E:</span> martin@corvell.co.uk
    </p>
  </section>
</main>
</body>
</html>
```